Moltbeck Chardonnay Wine Label 2024

We need a wine label design for a small, family-owned vineyard in Broke, Hunter Valley of NSW (Australia). The vineyard is called Moltbeck and we have an existing logo and 'brand book' for the vineyard home that is rented out for short stay bookings. This is attached and includes font style, colour palette and our Moltbeck logo for the accommodation (we're not wedded to this but also probably not after a completely different rethink either as we want the accommodation and the wine to feel part of the same thing.

Project:
The initial label requirement (front and back) is for the Moltbeck 2024 Chardonnay, which is called 'Juniper'. The label would need to be able to extend to other varietals (eg Verdehlo and Sparkling) in 2025. Attached is draft copy for front and back for the 2024 Chardonnay as a guide.

STYLE: We like a relatively simple, classic design and have played with both a dark (navy) and a light background (white/cream). Based on the final label design we will order a Kortap colour to pick up on the label theme.

The Chardonnay bottle dimensions are attached, as is our logo file (if that helps)

online 25-50 yearold

Wine

• front and back label design Moltbeck logo and name

```html
<!DOCTYPE html>
<html lang="en">
<head>
<meta charset="utf-8">
<title>Moltbeck Juniper 2024 Chardonnay – Front Label</title>
<link href="https://fonts.googleapis.com/css2?family=Josefin+Sans:wght@600&family=Source+Serif+4:wght@400;500&display=swap" rel="stylesheet">
<style>
  :root {
    --backdrop: #eeeeec;
    --label-paper: #ffffff;
    --contour-light: #f3f3f4;
    --contour-mid: #e4e5e8;
    --ink-navy: #2c3447;
    --vintage-taupe: #8c806a;
  }
  * { margin: 0; padding: 0; box-sizing: border-box; }
  html, body {
    width: 1200px;
    height: 1120px;
    overflow: hidden;
    background: var(--backdrop);
  }
  .canvas {
    width: 1200px;
    height: 1120px;
    display: flex;
    align-items: center;
    justify-content: center;
  }
  .front-label {
    position: relative;
    width: 820px;
    height: 900px;
    background: var(--label-paper);
    box-shadow: 0 2px 10px rgba(0,0,0,0.06);
    overflow: hidden;
  }
  .contour-field {
    position: absolute;
    inset: 0;
    background:
      radial-gradient(ellipse 40% 30% at 20% 55%, var(--contour-mid), transparent 70%),
      radial-gradient(ellipse 45% 35% at 80% 30%, var(--contour-mid), transparent 70%),
      radial-gradient(ellipse 50% 40% at 60% 85%, var(--contour-light), transparent 75%),
      var(--label-paper);
  }
  .label-content {
    position: relative;
    height: 100%;
    display: flex;
    flex-direction: column;
    align-items: center;
    color: var(--ink-navy);
    text-align: center;
  }
  .winery-name {
    margin-top: 170px;
    display: flex;
    align-items: center;
    gap: 22px;
    font-family: "Source Serif 4", Georgia, serif;
    font-weight: 400;
    font-size: 92px;
    letter-spacing: -0.5px;
    color: var(--ink-navy);
  }
  .winery-mark {
    width: 30px;
    height: 30px;
    border-radius: 50%;
    background: var(--ink-navy);
  }
  .wine-name {
    margin-top: 70px;
    font-family: "Josefin Sans", "Helvetica Neue", sans-serif;
    font-weight: 600;
    font-size: 62px;
    letter-spacing: 22px;
    padding-left: 22px;
  }
  .vintage {
    margin-top: 90px;
    font-family: "Source Serif 4", Georgia, serif;
    font-weight: 500;
    font-size: 58px;
    color: var(--vintage-taupe);
  }
  .varietal {
    margin-top: 6px;
    font-family: "Source Serif 4", Georgia, serif;
    font-weight: 500;
    font-size: 48px;
    letter-spacing: 9px;
    padding-left: 9px;
  }
  .region {
    margin-top: 22px;
    font-family: "Source Serif 4", Georgia, serif;
    font-weight: 500;
    font-size: 32px;
    letter-spacing: 5px;
    padding-left: 5px;
  }
  .volume {
    margin-top: 30px;
    font-family: "Source Serif 4", Georgia, serif;
    font-weight: 500;
    font-size: 46px;
  }
</style>
</head>
<body>
  <main class="canvas">
    <section class="front-label">
      <div class="contour-field" role="img" aria-label="Soft grey topographic contour line pattern across the label background"></div>
      <div class="label-content">
        <h1 class="winery-name">Moltbeck <span class="winery-mark"></span></h1>
        <h2 class="wine-name">JUNIPER</h2>
        <p class="vintage">2024</p>
        <p class="varietal">CHARDONNAY</p>
        <p class="region">HUNTER VALLEY</p>
        <p class="volume">750ml</p>
      </div>
    </section>
  </main>
</body>
</html>
```